Business Card Needed for Crafter of Pottery, Jewelry and Artwork

Calling all designers in search of an artistic challenge.

I need a new business card design for my pottery, jewelry and artwork business, Woven Glass and Tide, based in Vancouver BC.

I would like a card that is bright and inviting and preferably incorporates my logo and a sample of photos of my work while having a clean fresh look. The following contact details would preferably be included on the card as well:
• Helena Pikeworth
• Designer
• Phone: 604.555.0172
• Email: Designer@WovenGlassandTide.example
• Website: www.WovenGlassandTide.example
• Blog: www.ShapingHillside.example

The logo is attached in two color schemes in both Vector and Source formats. On past cards I’ve also included photos of my work. By including photos of the work the pieces are showcased and it catches people’s eye and prompts them to pick up the card and look at it more closely. For example, if I leave a stack in a coffee shop I want people to be drawn to the card, to pick it up and get a sense of the my product lines. Please feel free to pull photos of my work directly off of my website. If you need photos with higher pixels please let me know and I’ll email them directly to you. The website background is bffbda (191, 251, 218). I would like the business cards to match the feel of the website for consistency but the cards do not need to use the exact same colors. My website and current business card are predominantly turquoise shades. The background uses stripes provided by the website template. I don’t know the exact colors of the stripes.

My current business card is attached to show the use of photos in a design. Please note that I am not thrilled with my own design and am looking for variations and completely new designs. This example is not meant to be used as a template or starting point.

Here is some background surrounding my company:
WGT offers one of a kind jewelry, pottery, artwork and leather bags each designed with a twist. The pottery varies from rustic every day functional ware to raku artwork. The jewelry ranges from simple sterling every day pieces to multimedia pieces incorporating stone, metal, ceramics and fabric. The artwork is multimedia, typically acrylic paired with a natural element such as bark. All the bags are leather with reworked kimono fabric or patterned silk lining.

Feel free to check out my website to get a flavour for my work and the color scheme I've used on marketing materials so far. www.wovenglassandtide.example
Updates

Thank you to everyone who has submitted a design so far. I hope everyone has received some helpful feedback.

I'm going to post a survey to customers and friends asking for their votes. If you have new designs to submit please try to get them in by Saturday March 30 at noon so that I can include it in the survey launch.

Thank you

Target Market(s)

Females aged 25-65 interested in one of a kind functional pottery and jewelry.

Industry/Entity Type

Coffee Shop

Requirements
Must have
• Contact information, website, blog
Nice to have
• Logo, photos

```html
<!DOCTYPE html>
<html lang="en">
<head>
<meta charset="utf-8">
<title>Woven Glass and Tide — Business Card</title>
<link rel="stylesheet" href="https://fonts.googleapis.com/css2?family=Fira+Sans:wght@400;500&display=swap">
<style>
  :root {
    --page-bg: #e9ecea;
    --border-teal: #1fb6c4;
    --border-stripe: #2cc0cd;
    --panel-mint: #cfeee0;
    --ink-dark: #2b2b33;
    --ink-navy: #2c2f6e;
    --logo-teal: #17a9a6;
    --photo-dark: #6b4a3a;
    --photo-light: #b9cfc3;
  }
  * { box-sizing: border-box; margin: 0; padding: 0; }
  html, body {
    width: 1200px; height: 900px; overflow: hidden;
    background: var(--page-bg);
    font-family: "Fira Sans", Arial, sans-serif;
  }
  .sheet { position: relative; width: 1200px; height: 900px; }
  .card {
    position: absolute; left: 240px; width: 720px; height: 410px;
    border-radius: 6px;
    background: repeating-linear-gradient(90deg, var(--border-teal) 0 18px, var(--border-stripe) 18px 36px);
    box-shadow: 0 6px 18px rgba(0,0,0,0.18);
  }
  .card--front { top: 30px; }
  .card--back { top: 465px; }
  .card__panel {
    position: absolute; inset: 22px 24px;
    background: var(--panel-mint);
    border-radius: 10px;
    overflow: hidden;
  }
  .work-photo {
    position: absolute; left: 0; top: 0; width: 330px; height: 366px;
    background: linear-gradient(160deg, var(--photo-light) 0%, #a08272 55%, var(--photo-dark) 100%);
    opacity: 0.85;
  }
  .front-url {
    position: absolute; right: 30px; top: 200px;
    font-size: 19px; font-weight: 400; color: var(--ink-navy); letter-spacing: 0.3px;
    white-space: nowrap;
  }
  .brand {
    position: absolute; left: 26px; top: 24px;
    display: flex; align-items: center; gap: 14px;
  }
  .brand__dot {
    width: 110px; height: 110px; border-radius: 50%;
    background: var(--logo-teal);
  }
  .brand__name { font-size: 22px; font-weight: 500; color: var(--ink-navy); }
  .person { position: absolute; right: 130px; top: 160px; text-align: right; }
  .person__name { font-size: 29px; font-weight: 400; color: var(--ink-dark); letter-spacing: 0.4px; }
  .person__role { font-size: 18px; font-weight: 400; color: var(--ink-dark); margin-top: 6px; }
  .contacts {
    position: absolute; right: 20px; top: 250px;
    display: grid; grid-template-columns: auto 70px; column-gap: 18px; row-gap: 3px;
    font-size: 17px; line-height: 22px;
  }
  .contacts__value { color: var(--ink-dark); text-align: right; white-space: nowrap; }
  .contacts__label { color: var(--ink-navy); }
</style>
</head>
<body>
<main class="sheet">
  <section class="card card--front">
    <div class="card__panel">
      <div class="work-photo" role="img" aria-label="Photo of a handmade necklace of rough stone beads"></div>
      <p class="front-url">www.WovenGlassandTide.example</p>
    </div>
  </section>

  <section class="card card--back">
    <div class="card__panel">
      <div class="brand">
        <span class="brand__dot"></span>
        <span class="brand__name">Woven Glass and Tide</span>
      </div>
      <div class="person">
        <h1 class="person__name">Helena Pikeworth</h1>
        <p class="person__role">Designer</p>
      </div>
      <div class="contacts">
        <span class="contacts__value">604.555.0172</span><span class="contacts__label">tel</span>
        <span class="contacts__value">Designer@WovenGlassandTide.example</span><span class="contacts__label">email</span>
        <span class="contacts__value">www.WovenGlassandTide.example</span><span class="contacts__label">site</span>
        <span class="contacts__value">www.ShapingHillside.example</span><span class="contacts__label">blog</span>
      </div>
    </div>
  </section>
</main>
</body>
</html>
```